Patient Fact sheets for medical conditions and treatments

Hi,

I need a new design for my patient fact sheets. I am moving from my current clinic and I am looking from a new look.

I have attached
1. a current Fact sheet
2. New home page to the website
3. New Logo.

They need to be single page and easily readable for patients.

The will be in both PDF and print form in the future.

Target Market(s)

Patients with chronic pain age 40+

Font styles to use
Serif

Requirements
Must have
• My logo, should be inline with design elements on the Front page provided.

Please use the same font as the Logo

```html
<!DOCTYPE html>
<html lang="en">
<head>
<meta charset="utf-8">
<title>Platelet Rich Plasma (PRP) Therapy – Fact Sheet</title>
<link href="https://fonts.googleapis.com/css2?family=Crimson+Text:wght@400;600&family=Open+Sans:wght@400;600&family=Roboto:ital,wght@0,300;0,400;0,700;1,400;1,700&display=swap" rel="stylesheet">
<style>
  :root{
    --navy:#1d2357;
    --yellow:#f3c512;
    --backdrop:#7b7a85;
    --panel:#dfe1e6;
    --text:#3d3d45;
    --muted:#8a8a92;
    --white:#ffffff;
    --disclaimer-bg:#e9e9ec;
  }
  *{margin:0;padding:0;box-sizing:border-box}
  html,body{width:1200px;height:1200px;overflow:hidden;background:var(--backdrop)}
  .sheet{
    position:absolute;left:237px;top:57px;width:862px;height:1220px;
    background:var(--white);transform:scale(.8889);transform-origin:0 0;
    font-family:"Roboto",sans-serif;font-weight:300;color:var(--text);overflow:hidden;
  }
  .abs{position:absolute}
  .serif{font-family:"Crimson Text",serif;text-transform:uppercase;font-weight:400}

  .title-band{left:0;top:0;width:862px;height:50px;background:var(--navy);
    display:flex;align-items:center;justify-content:center;gap:16px}
  .title-band h1{font-family:"Crimson Text",serif;font-weight:400;color:var(--white);font-size:31px;letter-spacing:.3px}
  .title-band .rule{width:84px;height:1px;background:var(--white)}
  .title-line{left:0;top:50px;width:862px;height:5px;background:var(--yellow)}

  .photo{left:360px;top:60px;width:502px;height:315px;
    background:linear-gradient(120deg,#c9ccd2 0%,#e9eaed 45%,#f0d45a 60%,#e6e8ec 75%,#d5d8dd 100%);
    clip-path:polygon(0 0,100% 0,100% 100%,60px 100%)}

  .doctor-name{left:40px;top:78px;width:330px;font-family:"Crimson Text",serif;font-size:30px;color:var(--navy);letter-spacing:1px}

  .fact-back{left:0;top:152px;width:425px;height:60px;background:var(--navy);clip-path:polygon(0 0,100% 0,100% 100%,0 100%)}
  .fact-band{left:0;top:152px;width:405px;height:54px;background:var(--yellow);clip-path:polygon(0 0,392px 0,100% 100%,0 100%)}
  .fact-band span{position:absolute;left:53px;top:-2px;font-family:"Open Sans",sans-serif;font-weight:600;color:var(--white);font-size:46px;letter-spacing:.5px}

  .what-is{left:0;top:206px;width:470px;height:207px;background:var(--navy);clip-path:polygon(0 0,420px 0,100% 100%,0 100%);padding:16px 0 0 17px}
  .what-is h2{color:var(--yellow);font-size:24px;line-height:1}
  .what-is p{color:var(--white);font-size:15px;line-height:17.5px;margin-top:7px;width:430px}
  .accent-tri{left:465px;top:373px;width:45px;height:40px;background:var(--yellow);clip-path:polygon(0 0,100% 0,20% 100%)}

  .how h2{left:22px;top:423px;font-size:21px;color:var(--navy)}
  .how-rule{left:0;top:449px;width:258px;height:3px;background:var(--yellow)}
  .how p{left:22px;top:455px;width:816px;font-size:14.6px;line-height:17.4px;text-align:justify}

  .role-panel{left:0;top:628px;width:565px;height:320px;background:var(--panel);clip-path:polygon(0 0,495px 0,100% 100%,0 100%)}
  .role-head{left:0;top:628px;width:490px;height:66px;background:var(--navy);clip-path:polygon(0 0,478px 0,100% 100%,0 100%);padding:9px 0 0 22px}
  .role-head h2{color:var(--yellow);font-size:24px;line-height:26px}
  .role-body{left:22px;top:708px;width:480px;font-size:14.6px;line-height:17.4px}
  .role-body ul{list-style:none;margin-top:17px}
  .role-body li{position:relative;padding-left:11px}
  .role-body li::before{content:"";position:absolute;left:0;top:5px;border-left:5px solid var(--navy);border-top:4px solid transparent;border-bottom:4px solid transparent}

  .results-tab{left:0;top:895px;width:540px;height:50px;background:var(--white);clip-path:polygon(0 0,530px 0,100% 100%,0 100%);padding:10px 0 0 16px}
  .results-tab h2{font-size:23px;color:var(--navy)}

  .treat h2{right:24px;top:635px;font-size:21px;color:var(--navy)}
  .treat-rule{left:597px;top:660px;width:265px;height:3px;background:var(--yellow)}
  .treat .lead{right:24px;top:671px;font-size:14.6px}
  .treat ul{right:24px;top:705px;list-style:none;text-align:right;font-weight:700;color:var(--navy);font-size:14.6px;line-height:17.4px}
  .treat li svg{width:12px;height:11px;margin-right:5px;vertical-align:0}
  .treat .ask{right:24px;top:880px;text-align:right;font-style:italic;font-weight:700;color:var(--muted);font-size:14.6px;line-height:17.4px}

  .results-band{left:0;top:945px;width:862px;height:94px;background:var(--yellow);padding:12px 22px 0 20px}
  .results-band p{font-size:14.6px;line-height:17.4px;color:var(--navy);font-weight:400;text-align:justify}

  .footer-navy{left:298px;top:1039px;width:564px;height:109px;background:var(--navy);clip-path:polygon(22px 0,100% 0,100% 100%,0 100%)}
  .clinic-name{left:40px;top:1077px;font-family:"Roboto",sans-serif;font-weight:400;color:var(--navy);font-size:24px;display:flex;align-items:center;gap:8px}
  .clinic-name i{display:block;width:14px;height:14px;border-radius:50%;background:var(--yellow)}
  .contact{left:352px;top:1050px;color:var(--white);font-size:15.6px;line-height:20.5px;font-weight:400}
  .contact .more{color:var(--yellow);font-weight:700;font-style:italic;font-size:16.5px;margin-left:22px}
  .contact .org{font-weight:700;margin-left:22px}
  .contact .row{display:flex;align-items:center;gap:6px}
  .contact svg{width:14px;height:14px;flex:none}
  .contact .gap{margin-left:24px}

  .disclaimer{left:0;top:1148px;width:862px;height:72px;background:var(--disclaimer-bg);padding:10px 16px 0 24px;font-size:10.2px;line-height:12.8px;font-style:italic;font-weight:400;color:#55555c}
  .disclaimer b{font-weight:700}
</style>
</head>
<body>
<main class="sheet">
  <header class="abs title-band"><span class="rule"></span><h1>PLATELET RICH PLASMA (PRP) THERAPY</h1><span class="rule"></span></header>
  <div class="abs title-line"></div>

  <div class="abs photo" role="img" aria-label="Gloved hand holding two test tubes of yellow plasma"></div>
  <div class="abs doctor-name">Dr Alan Reeve</div>

  <div class="abs fact-back"></div>
  <div class="abs fact-band"><span>FACT SHEET</span></div>

  <section class="abs what-is">
    <h2 class="serif">What is PRP?</h2>
    <p>Platelet-Rich Plasma (PRP) is concentrated platelets and white blood cells derived from your own blood. Platelet Rich Plasma Injection Therapy (PRP therapy), is a growing treatment approach for soft tissue injuries including tendon, muscle &amp; ligaments. It is also showing good results for mild to moderate osteoarthritis. While this approach has been used overseas for many years, it’s fairly new to Australia in the treatment of musculoskeletal and orthopaedic conditions.</p>
  </section>
  <div class="abs accent-tri"></div>

  <section class="how">
    <h2 class="abs serif">How does PRP work?</h2>
    <div class="abs how-rule"></div>
    <p class="abs">Some tissues in the body have a poor blood supply or respond poorly to excessive load, ultimately failing to heal naturally. While some of our primary treatment such as physiotherapy, massage, biomechanical correction &amp; other forms of treatment are used to treat these soft tissue injuries, sometimes the body fails to respond. PRP therapy utilises the healing properties in blood to allow a healing reaction to occur in a tissue that’s not healing on its own. Our blood has small granules called ‘platelets’, which contain special growth factors that when released, allow stem cells in the particular tissue to ‘switch’ on and cause new tissue to be created and heal the injured area. Take the example of achilles tendinopathy. If the achilles is painful, thickened and not responding to rehabilitation, then the sports physician will inject the PRP into the achilles which will cause the tendon cells (tenocytes/fibroblasts) to create new achilles collagen to strengthen the achilles. White blood cells also enter the area to mop up any achilles tissue that may have been damaged due to the ongoing pain and thickening in the area.</p>
  </section>

  <div class="abs role-panel"></div>
  <div class="abs role-head"><h2 class="serif">Role of platelets<br>and growth factors</h2></div>
  <div class="abs role-body">
    <p>PRP contains highly concentrated platelets. Platelets have been identified to secrete growth factors, which are known to play a role in:</p>
    <ul>
      <li>Increasing tissue vascularity and increasing the rate of pithelial tissue production (wound healing)</li>
      <li>Attracting other cells that fight infection</li>
      <li>Acting as a seal during closures</li>
      <li>Providing an immediate surgical hemostatic agent (reduction of bleeding)</li>
      <li>Osteogenesis (bone regeneration and repair).</li>
    </ul>
  </div>

  <div class="abs results-tab"><h2 class="serif">What are the expected results of PRP?</h2></div>

  <section class="treat">
    <h2 class="abs serif">What can PRP treat?</h2>
    <div class="abs treat-rule"></div>
    <p class="abs lead">PRP therapy can be used for:</p>
    <ul class="abs">
      <li><svg viewBox="0 0 12 11"><path d="M1 6l3.5 3.5L11 1" fill="none" stroke="#f3c512" stroke-width="2"/></svg>Orthopedic surgery</li>
      <li><svg viewBox="0 0 12 11"><path d="M1 6l3.5 3.5L11 1" fill="none" stroke="#f3c512" stroke-width="2"/></svg>Cardiac surgery</li>
      <li><svg viewBox="0 0 12 11"><path d="M1 6l3.5 3.5L11 1" fill="none" stroke="#f3c512" stroke-width="2"/></svg>Plastic and cosmetic surgery</li>
      <li><svg viewBox="0 0 12 11"><path d="M1 6l3.5 3.5L11 1" fill="none" stroke="#f3c512" stroke-width="2"/></svg>Ear, nose, throat (ENT) surgery</li>
      <li><svg viewBox="0 0 12 11"><path d="M1 6l3.5 3.5L11 1" fill="none" stroke="#f3c512" stroke-width="2"/></svg>Oral maxillofacial surgery</li>
      <li><svg viewBox="0 0 12 11"><path d="M1 6l3.5 3.5L11 1" fill="none" stroke="#f3c512" stroke-width="2"/></svg>Neurosurgery</li>
      <li><svg viewBox="0 0 12 11"><path d="M1 6l3.5 3.5L11 1" fill="none" stroke="#f3c512" stroke-width="2"/></svg>Vascular surgery</li>
      <li><svg viewBox="0 0 12 11"><path d="M1 6l3.5 3.5L11 1" fill="none" stroke="#f3c512" stroke-width="2"/></svg>Wound healing</li>
      <li><svg viewBox="0 0 12 11"><path d="M1 6l3.5 3.5L11 1" fill="none" stroke="#f3c512" stroke-width="2"/></svg>Burn care</li>
    </ul>
    <p class="abs ask">Ask your doctor whether<br>plateletric plasma is appropriate<br>for your surgical procedure</p>
  </section>

  <section class="abs results-band">
    <p>Because the goal of PRP therapy is to resolve pain through healing, it could prove to have lasting results. Initial improvement may be seen within a few weeks, gradually increasing as the healing progresses. Research studies &amp; clinical practice have shown PRP therapy to be very effective at relieving pain and returning patients to their normal lives. The need for surgery can also be greatly reduced by treating injured tissues before the damage progresses and the condition is irreversible.</p>
  </section>

  <div class="abs clinic-name"><i></i>Northgate Pain Clinic</div>
  <div class="abs footer-navy"></div>
  <address class="abs contact" style="font-style:normal">
    <div class="more">For more information</div>
    <div class="org">Northgate Pain Clinic</div>
    <div class="row"><svg viewBox="0 0 14 14"><path d="M7 1a4 4 0 0 0-4 4c0 3 4 8 4 8s4-5 4-8a4 4 0 0 0-4-4zm0 5.5A1.5 1.5 0 1 1 7 3.5a1.5 1.5 0 0 1 0 3z" fill="#f3c512"/></svg>Harbour House, Ground Floor, 48 Elm Street, Kelvin VIC 3170</div>
    <div class="row">
      <svg viewBox="0 0 14 14"><path d="M3 1.5l2 2.5-1 1.5c.8 1.8 2 3 3.5 3.8l1.5-1 2.5 2-1.2 2C6 11.5 2.5 8 1.2 2.7z" fill="#f3c512"/></svg>03 9000 4821
      <svg class="gap" viewBox="0 0 14 14"><rect x="3" y="1" width="8" height="4" fill="#f3c512"/><rect x="1" y="5" width="12" height="6" rx="1" fill="#f3c512"/><rect x="3.5" y="8.5" width="7" height="4.5" fill="#f3c512" stroke="#1d2357" stroke-width="1"/></svg>03 9000 4822
      <svg class="gap" viewBox="0 0 14 14"><rect x="1" y="3" width="12" height="8" fill="none" stroke="#f3c512" stroke-width="1.3"/><path d="M1 3l6 5 6-5" fill="none" stroke="#f3c512" stroke-width="1.3"/></svg>info@northgatepain.com.au
    </div>
  </address>

  <footer class="abs disclaimer">
    <b>DISCLAIMER:</b> Please note the contents contained in this Patient Fact Sheet are not intended as a substitute for your own independent health professional’s advice, diagnosis or treatment. At Northgate Pain Clinic, we assess every patient’s condition individually. As leaders in pain intervention, we aim to provide advanced, innovative, &amp; evidence-based treatments tailored to suit each patient. As such, recommended treatments and their outcomes will vary from patient to patient. If you would like to find out whether our treatments are suitable for your specific condition, please speak to one of our doctors at the time of your consultation.
  </footer>
</main>
</body>
</html>
```